College Admissions Consulting needs a small street facing sign for new office location.

I need a graphic design to be used inside window for a banner/sign in office location on a high walking traffic city street, for my company, Campus Compass. I work with high school students and families on the college planning and selection application process. Please check out the website to learn more about what I do (www.myfernleaprep.com). The banner will be used to market our services at our office location. The final design should utilize logo colors, phone number, and website/email information. I'd like to incorporate a my picture in someway because of face recognition. To be printed on a posterboard or vinyl banner.

Target Market(s)

Parents of high school aged children.

Industry/Entity Type

Education

Font styles to use
Sans Serif

Colors
abd037

Requirements
Must have
• Clean, attractive, and professional design. Attract the attention of people walking by. Information must be clear and readable (phone/email, etc.).
Nice to have
• Utilize the picture with crossed arms (without the brown background on picture).
Emphasize tagline:
Mastering The College Admission Process
....with personalized, professional guidance in planning, selecting, and applying to the right colleges.

```html
<!DOCTYPE html>
<html lang="en">
<head>
<meta charset="utf-8">
<title>Campus Compass – Window Banner</title>
<link rel="stylesheet" href="https://fonts.googleapis.com/css2?family=Montserrat:wght@500;600;700&display=swap">
<style>
  :root {
    --backdrop: #e4e4e4;
    --charcoal: #4b4b4e;
    --lime: #86c934;
    --lime-light: #b9e48c;
    --lime-text: #8fd13a;
    --ink: #4a4a4d;
    --white: #ffffff;
    --photo-dark: #2a2320;
    --photo-mid: #5a3f33;
  }
  * { margin: 0; padding: 0; box-sizing: border-box; }
  html, body {
    width: 1200px; height: 1200px; overflow: hidden;
    background: var(--backdrop);
    font-family: "Montserrat", Arial, sans-serif;
  }
  .banner {
    position: absolute; left: 48px; top: 241px;
    width: 1105px; height: 738px;
    background: var(--charcoal);
    overflow: hidden;
  }
  .header { position: absolute; left: 0; top: 0; width: 100%; height: 212px; background: var(--charcoal); }
  .brand-dot {
    position: absolute; left: 40px; top: 30px;
    width: 110px; height: 110px; border-radius: 50%;
    background: var(--lime);
  }
  .brand-name {
    position: absolute; left: 198px; top: 46px;
    font-size: 56px; line-height: 1; font-weight: 500; color: var(--white);
    white-space: nowrap;
  }
  .divider { position: absolute; left: 0; top: 212px; width: 100%; height: 4px; background: var(--lime); }
  .hero {
    position: absolute; left: 0; top: 225px; width: 100%; height: 353px;
    background: radial-gradient(circle at 78% 45%, var(--lime-light) 0%, var(--lime) 45%);
    overflow: hidden;
  }
  .hero-rings { position: absolute; inset: 0; }
  .headline {
    position: absolute; left: 0; top: 14px; width: 758px;
    text-align: center; color: var(--white);
    font-size: 60px; font-weight: 700; line-height: 61px; letter-spacing: -0.3px;
  }
  .tagline {
    position: absolute; left: 0; top: 204px; width: 758px;
    text-align: center; color: var(--ink);
    font-size: 34px; font-weight: 600; line-height: 38px;
  }
  .portrait {
    position: absolute; left: 732px; top: 8px;
    width: 329px; height: 570px;
    border-radius: 160px 160px 0 0;
    background: linear-gradient(180deg, var(--photo-mid) 0%, var(--photo-dark) 40%, #1b1b1c 100%);
  }
  .footer { position: absolute; left: 0; top: 578px; width: 100%; height: 160px; }
  .footer-slash { position: absolute; left: 0; top: 0; }
  .offer {
    position: absolute; left: 36px; top: 22px;
    font-size: 46px; line-height: 1; font-weight: 700; color: var(--lime-text); white-space: nowrap;
  }
  .phone {
    position: absolute; left: 36px; top: 78px;
    font-size: 49px; line-height: 1; font-weight: 700; color: var(--white); white-space: nowrap;
  }
  .consultant {
    position: absolute; left: 669px; top: 10px;
    font-size: 56px; line-height: 1; font-weight: 700; color: var(--lime-text);
    letter-spacing: 1px; white-space: nowrap;
  }
  .contact {
    position: absolute; left: 640px; display: flex; align-items: center; gap: 10px;
    font-size: 28px; line-height: 1; font-weight: 500; color: var(--white); white-space: nowrap;
  }
  .contact-email { top: 78px; }
  .contact-web { top: 114px; }
  .contact .accent { color: var(--lime-text); }
  .contact svg { width: 22px; height: 22px; flex: none; }
</style>
</head>
<body>
  <main class="banner">
    <header class="header">
      <span class="brand-dot"></span>
      <span class="brand-name">Campus Compass</span>
    </header>
    <div class="divider"></div>

    <section class="hero">
      <svg class="hero-rings" width="1105" height="353" viewBox="0 0 1105 353" aria-hidden="true">
        <circle cx="385" cy="100" r="185" fill="none" stroke="#7cbf2e" stroke-width="22" opacity="0.35"/>
        <circle cx="880" cy="20" r="145" fill="none" stroke="#7cbf2e" stroke-width="18" opacity="0.3"/>
        <circle cx="760" cy="410" r="195" fill="none" stroke="#7cbf2e" stroke-width="16" opacity="0.25"/>
      </svg>
      <h1 class="headline">MASTERING THE<br>COLLEGE ADMISSION<br>PROCESS</h1>
      <p class="tagline">...with personalized, professional<br>guidance in planning, selecting, and<br>applying to the right colleges.</p>
    </section>

    <div class="portrait" role="img" aria-label="Portrait photo of the consultant smiling, arms crossed, in a black top"></div>

    <footer class="footer">
      <svg class="footer-slash" width="1105" height="160" viewBox="0 0 1105 160" aria-hidden="true">
        <line x1="638" y1="0" x2="574" y2="160" stroke="#ffffff" stroke-width="4"/>
      </svg>
      <p class="offer">FREE CONSULTATION</p>
      <p class="phone">412-555-PREP (7737)</p>
      <p class="consultant">NORA BLAKE</p>
      <p class="contact contact-email">
        <svg viewBox="0 0 24 24" aria-hidden="true"><rect x="2" y="6" width="20" height="14" fill="none" stroke="#8fd13a" stroke-width="2"/><path d="M2 6l10 8 10-8" fill="none" stroke="#8fd13a" stroke-width="2"/></svg>
        nora@myfernleaprep.com
      </p>
      <p class="contact contact-web">
        <svg viewBox="0 0 24 24" aria-hidden="true"><circle cx="12" cy="12" r="9" fill="none" stroke="#8fd13a" stroke-width="2"/><ellipse cx="12" cy="12" rx="4" ry="9" fill="none" stroke="#8fd13a" stroke-width="1.6"/><line x1="3" y1="12" x2="21" y2="12" stroke="#8fd13a" stroke-width="1.6"/></svg>
        <span>www.<span class="accent">myfernleaprep</span>.com</span>
      </p>
    </footer>
  </main>
</body>
</html>
```